Startup FinTech / Behavioural Science company needs website redesign

We are a startup company interested in redesigning our website. We have most of our content created already (viewable at www.tallyfern.co), but are interested in an upgraded look and feel. We are happy to adjust content as well based on design input. We will move hosting from hostbirch to webmarlo or similar hosting service, so portability of files is important to us. Our team will have the ability to make minor tweaks/content adjustments, but would look to engage with someone for more-comprehensive enhancements in the future.
Updates

Project Deadline Extended
Reason: Other business needs prevented me from providing timely feedback. I will work on feedback over the next two days but wanted to give additional time for design submissions and revisions.

Target Market(s)

Financial advisors in the US and UK, as well as potential end-users of the tools and potential investors

Industry/Entity Type

Information Technology

Coding

Coded - Design and coding required

Number of Pages Required

1 page

Font styles to use
Sans Serif

Requirements
Must have
• - Lighter, cleaner look and feel. We believe our current website is too heavy and "angular."
• - improved iconography to convey behavioural finance concepts (e.g., herd mentality, and illusion of control)
• - links to social media sites
• - integration with our hostbirch personality profile (viewable now at https://deanmollow.formquill.com/to/qRtZbe. Note: we will change this URL to tallyfern.formquill.com... as a part of the design process)
Nice to have
• - ability for us to add a tab/link to a blog in the future.
• - design that allows us to add additional
• - ability for us to add additional pages (e.g., results from our personality profiles, pages to customize sharing on social media)
• - simple ability to enter an email address to add to our mailing list/request more info
• - mobile-responsive design
Should not have
• - Should not have items like office directions and maps, since we are a virtual team.
• - Contact information (e.g., phone number) should be lower down the page vs. at the top
• - comments boxes or lengthy web forms. A simple name/email address is sufficient.

```html
<!DOCTYPE html>
<html lang="en">
<head>
<meta charset="utf-8">
<title>Tallyfern — FinTech &amp; Behavioural Science</title>
<link href="https://fonts.googleapis.com/css2?family=Montserrat:wght@400;600;700&family=Open+Sans:wght@400;600&display=swap" rel="stylesheet">
<style>
:root{
  --purple:#8a2c9c;
  --ink:#333333;
  --muted:#8a8a8a;
  --line:#e3e3e3;
  --panel:#efefef;
  --band:#f2f2f2;
  --white:#ffffff;
}
*{box-sizing:border-box;margin:0;padding:0}
html,body{width:1200px;height:2872px;overflow:hidden;background:var(--white)}
body{font-family:"Open Sans",Arial,sans-serif;color:var(--ink);position:relative}

.site-header{position:absolute;top:0;left:0;width:1200px;height:112px}
.brand{position:absolute;left:128px;top:24px;display:flex;align-items:center;gap:10px;font-family:"Montserrat",Arial,sans-serif;font-weight:700;font-size:38px;color:var(--ink);letter-spacing:-.5px}
.brand-dot{width:14px;height:14px;border-radius:50%;background:var(--purple)}
.header-phone{position:absolute;right:132px;top:20px;font-size:15px;color:var(--ink);display:flex;align-items:center;gap:8px}
.header-phone svg{width:18px;height:18px}
.main-nav{position:absolute;right:132px;top:70px;display:flex;gap:30px;font-family:"Montserrat",Arial,sans-serif;font-size:11px;font-weight:600;letter-spacing:.5px}
.main-nav a{color:var(--ink);text-decoration:none}
.main-nav a.active{color:var(--purple)}

.hero{position:absolute;top:112px;left:0;width:1200px;height:488px;background:linear-gradient(100deg,#c9c3bb 0%,#ddd8d1 30%,#9c9a97 60%,#55585c 100%)}
.hero-photo{position:absolute;inset:0}
.hero-shade{position:absolute;inset:0;background:rgba(60,50,70,.25)}
.hero-title{position:absolute;left:430px;width:620px;top:318px;text-align:center;color:var(--white);font-family:"Montserrat",Arial,sans-serif;font-weight:700;font-size:36px;line-height:44px;letter-spacing:1px}
.btn{display:inline-block;background:var(--purple);color:var(--white);font-family:"Montserrat",Arial,sans-serif;font-weight:600;font-size:12px;letter-spacing:1px;text-decoration:none}
.hero .btn{position:absolute;left:662px;top:410px;width:156px;height:34px;line-height:34px;text-align:center}

.section-title{position:absolute;left:0;width:1200px;text-align:center;font-family:"Montserrat",Arial,sans-serif;font-weight:600;font-size:30px;line-height:38px;letter-spacing:1px}
.welcome-title{top:612px;color:var(--purple)}
.welcome-text{position:absolute;left:290px;width:620px;top:666px;text-align:center;font-size:11px;line-height:18px;color:var(--muted)}
.topics{position:absolute;top:780px;left:132px;display:flex;gap:58px}
.topic{width:268px;height:180px;background:var(--panel);text-align:center;padding-top:42px}
.topic svg{width:60px;height:60px}
.topic-label{margin-top:18px;font-family:"Montserrat",Arial,sans-serif;font-weight:600;font-size:15px;letter-spacing:1.5px;color:var(--purple)}
.divider{position:absolute;left:132px;width:936px;top:1020px;border-top:1px solid var(--line)}

.solution-title{top:1070px;color:var(--ink)}
.mascot{position:absolute;left:460px;top:1188px;width:280px;height:280px;border-radius:50%;background:radial-gradient(circle,#8a2c9c 0 38%,#2e2e2e 39% 100%)}
.step{position:absolute;width:320px}
.step svg{width:30px;height:30px;display:block}
.step h3{font-family:"Montserrat",Arial,sans-serif;font-weight:700;font-size:18px;line-height:24px;color:var(--ink);letter-spacing:.8px;margin-top:14px}
.step p{font-size:10px;line-height:16px;color:var(--muted);margin-top:10px}
.step.left{left:100px;text-align:right}
.step.left svg{margin-left:auto}
.step.right{left:780px;text-align:left}
.s1,.s2{top:1152px}
.s3,.s4{top:1372px}

.team{position:absolute;top:1580px;left:0;width:1200px;height:632px;background:var(--band)}
.team-title{top:54px;color:var(--ink)}
.member{position:absolute;top:132px;width:288px;height:428px;background:var(--white);border:1px solid var(--line);text-align:center}
.m1{left:296px}.m2{left:616px}
.portrait{width:176px;height:176px;border-radius:50%;margin:24px auto 0;background:linear-gradient(160deg,#e6e4e1,#a9a7a5);border:4px solid #ececec}
.member h3{margin-top:52px;font-family:"Montserrat",Arial,sans-serif;font-weight:600;font-size:18px;color:var(--purple);letter-spacing:1px}
.member p{margin:14px auto 0;width:220px;font-size:10px;line-height:16px;color:var(--muted)}
.dots{display:flex;justify-content:center;gap:12px;margin-top:24px}
.dots span{width:10px;height:10px;border-radius:50%;background:#8d8d8d}

.contact-title{top:2270px;color:var(--ink)}
.contact-form{position:absolute;top:2328px;left:360px;width:480px}
.field{background:var(--panel);font-size:10px;color:var(--muted);padding:10px 12px}
.row{display:flex;gap:8px}
.row .field{width:236px;height:40px}
.msg{width:480px;height:104px;margin-top:16px}
.contact-form .btn{margin-top:22px;width:104px;height:32px;line-height:32px;text-align:center}

.site-footer{position:absolute;top:2592px;left:0;width:1200px;height:280px;background:#f7f7f7;border-top:1px solid var(--line)}
.footer-brand{position:absolute;left:128px;top:40px;display:flex;align-items:center;gap:8px;font-family:"Montserrat",Arial,sans-serif;font-weight:700;font-size:34px;color:var(--ink)}
.footer-brand .brand-dot{width:12px;height:12px}
.footer-dots{position:absolute;left:132px;top:98px;display:flex;gap:8px}
.footer-dots span{width:24px;height:24px;border-radius:50%;border:2px solid var(--ink)}
.fcol{position:absolute;top:44px}
.fcol h4{font-family:"Montserrat",Arial,sans-serif;font-weight:700;font-size:10px;color:var(--purple);letter-spacing:.8px;margin-bottom:14px}
.fcol li{list-style:none;font-size:10px;line-height:19px;color:var(--muted)}
.fcol p{font-size:10px;line-height:16px;color:var(--muted);width:200px}
.c1{left:400px}.c2{left:560px}.c3{left:898px}
.select{margin-top:16px;width:200px;height:28px;background:var(--white);border:1px solid var(--line);font-size:10px;color:var(--muted);padding:6px 10px}
.c3 li{display:flex;align-items:center;gap:8px}
.c3 svg{width:11px;height:11px}
.footer-rule{position:absolute;left:128px;right:128px;top:218px;border-top:1px solid var(--line)}
.copyright{position:absolute;left:0;width:1200px;top:238px;text-align:center;font-size:9px;color:var(--muted)}
</style>
</head>
<body>

<header class="site-header">
  <div class="brand"><span>tallyfern</span><span class="brand-dot"></span></div>
  <div class="header-phone">
    <svg viewBox="0 0 24 24"><circle cx="12" cy="12" r="11" fill="var(--purple)"/><path d="M8.5 6.5l2 2-1.2 1.6c.8 1.6 2 2.8 3.6 3.6l1.6-1.2 2 2-1.5 1.8C11 16 8 13 6.7 8z" fill="#fff"/></svg>
    +1 555 014 2290
  </div>
  <nav class="main-nav">
    <a class="active" href="#">THE PROBLEM</a><a href="#">THE SOLUTION</a><a href="#">OUR TEAM</a><a href="#">TAKE PROFILE</a><a href="#">CONTACT</a>
  </nav>
</header>

<section class="hero">
  <div class="hero-photo" role="img" aria-label="Photo of a smiling businesswoman in an office with a colleague"></div>
  <div class="hero-shade"></div>
  <h1 class="hero-title">FINTECH &amp; BEHAVIOURAL<br>SCIENCE</h1>
  <a class="btn" href="#">LEARN MORE</a>
</section>

<h2 class="section-title welcome-title">WELCOME TO TALLYFERN</h2>
<p class="welcome-text">Tallyfern blends financial tools with behavioural science. We help people see the habits that shape their money, and give advisors clear insight into choices, biases and goals — so each plan fits the person behind it.</p>

<div class="topics">
  <div class="topic">
    <svg viewBox="0 0 60 60" fill="none" stroke="#555" stroke-width="5"><circle cx="22" cy="30" r="13"/><circle cx="38" cy="30" r="13"/></svg>
    <div class="topic-label">DIVORCE</div>
  </div>
  <div class="topic">
    <svg viewBox="0 0 60 60" fill="#555"><path d="M18 10h16l-3 30h-10z"/><rect x="20" y="42" width="12" height="4"/><rect x="38" y="20" width="8" height="26" rx="2"/><rect x="40" y="14" width="4" height="6"/></svg>
    <div class="topic-label">ADDICTION</div>
  </div>
  <div class="topic">
    <svg viewBox="0 0 60 60" fill="#555"><rect x="12" y="16" width="36" height="34" rx="6"/><circle cx="30" cy="30" r="9" fill="var(--panel)"/><path d="M30 30l4-6" stroke="#555" stroke-width="2"/></svg>
    <div class="topic-label">OBESITY</div>
  </div>
</div>
<div class="divider"></div>

<h2 class="section-title solution-title">OUR SOLUTION</h2>
<div class="mascot" role="img" aria-label="Purple owl mascot illustration in a dark circle"></div>

<div class="step left s1">
  <svg viewBox="0 0 30 30" fill="none" stroke="#777" stroke-width="2"><path d="M6 3h14l5 5v19H6z"/><path d="M20 3v5h5"/></svg>
  <h3>TAKE THE PROFILE</h3>
  <p>Take the Tallyfern profile to learn more about your financial personality and tendencies.</p>
</div>
<div class="step right s2">
  <svg viewBox="0 0 30 30" fill="#777"><circle cx="22" cy="6" r="4"/><circle cx="8" cy="15" r="4"/><circle cx="22" cy="24" r="4"/><path d="M8 15L22 6M8 15l14 9" stroke="#777" stroke-width="2"/></svg>
  <h3>CONNECT ACCOUNTS</h3>
  <p>Link your Tallyfern profile to your accounts to track your financial decisions and tendencies.</p>
</div>
<div class="step left s3">
  <svg viewBox="0 0 30 30" fill="#777"><path d="M3 27V16l7-6 6 5 8-9 3 3v18z"/></svg>
  <h3>GAIN BETTER INSIGHT</h3>
  <p>See what drives your choices and learn more about your financial personality and tendencies.</p>
</div>
<div class="step right s4">
  <svg viewBox="0 0 30 30" fill="none" stroke="#777" stroke-width="2"><path d="M3 14L27 4 21 26l-6-8z"/><path d="M15 18L27 4"/></svg>
  <h3>CHECK YOUR PROGRESS</h3>
  <p>Revisit your Tallyfern profile to see how your financial habits and tendencies have changed.</p>
</div>

<section class="team">
  <h2 class="section-title team-title">OUR TEAM</h2>
  <article class="member m1">
    <div class="portrait" role="img" aria-label="Portrait photo of team member Dean Mollow"></div>
    <h3>DEAN MOLLOW, CFA</h3>
    <p>Founder, former investment portfolio manager. Lecturer, behavioural finance. Based in London.</p>
    <div class="dots"><span></span><span></span><span></span></div>
  </article>
  <article class="member m2">
    <div class="portrait" role="img" aria-label="Portrait photo of team member Owen Lasky"></div>
    <h3>OWEN LASKY</h3>
    <p>Co-founder, former product design manager. Lecturer, decision science. Based in Boston.</p>
    <div class="dots"><span></span><span></span><span></span></div>
  </article>
</section>

<h2 class="section-title contact-title">GET IN TOUCH</h2>
<form class="contact-form">
  <div class="row"><div class="field">Name</div><div class="field">Email</div></div>
  <div class="field msg">Message</div>
  <a class="btn" href="#">SUBMIT</a>
</form>

<footer class="site-footer">
  <div class="footer-brand"><span>tallyfern</span><span class="brand-dot"></span></div>
  <div class="footer-dots"><span></span><span></span><span></span></div>
  <div class="fcol c1">
    <h4>QUICK LINKS</h4>
    <ul><li>Home</li><li>The Problem</li><li>The Solution</li><li>Our Team</li><li>Take Profile</li></ul>
  </div>
  <div class="fcol c2">
    <h4>NEWSLETTER</h4>
    <p>Enter your email address to receive the latest news and updates from our team.</p>
    <div class="select">Enter Your Email</div>
  </div>
  <div class="fcol c3">
    <h4>CONTACT US</h4>
    <ul>
      <li><svg viewBox="0 0 12 12"><circle cx="6" cy="6" r="6" fill="#555"/></svg>+1 555 014 2290</li>
      <li><svg viewBox="0 0 12 12"><circle cx="6" cy="6" r="6" fill="#555"/></svg>+44 20 7946 0118</li>
      <li><svg viewBox="0 0 12 12"><rect x="0" y="2" width="12" height="8" fill="#555"/></svg>hello@tallyfern.co</li>
    </ul>
  </div>
  <div class="footer-rule"></div>
  <p class="copyright">© 2017 Tallyfern Ltd — All Rights Reserved</p>
</footer>

</body>
</html>
```